New Webpage for High Class Expert Witness Services Company

We are looking for a minimalist design for a webpage that just has our logo and an entry form offer to connect with one of our Liaisons.
The entry form should just ask for Name, Email, Contact Info and Description of Project.

Company Name is: The Marlow Crest Advisory Services

Number of Pages Required

1 page

```html
<!DOCTYPE html>
<html lang="en">
<head>
<meta charset="utf-8">
<title>Marlow Crest Advisory Services — Connect with a Liaison</title>
<link href="https://fonts.googleapis.com/css2?family=Cinzel:wght@400;600&family=Roboto:wght@400&display=swap" rel="stylesheet">
<style>
  :root {
    --bg-deep: #060606;
    --bg-mid: #1c1c1d;
    --text-bright: #f2f2f2;
    --text-muted: #a7a7a7;
    --line: #8a8a8a;
    --input-border: #cfcfcf;
    --input-text: #e4e4e4;
    --button-light: #e2e2e4;
    --button-dark: #9b9b9f;
    --button-text: #111;
    --footer-text: #9a9a9a;
    --rule: #333;
  }
  * { box-sizing: border-box; margin: 0; padding: 0; }
  html, body { width: 1200px; height: 742px; overflow: hidden; background: var(--bg-deep); }
  .page { position: relative; width: 1200px; height: 742px; overflow: hidden; }
  .backdrop {
    position: absolute; inset: 0;
    background:
      radial-gradient(ellipse 420px 380px at 300px 330px, var(--bg-mid) 0%, rgba(20,20,21,0.6) 45%, transparent 80%),
      radial-gradient(ellipse 700px 500px at 900px 380px, #111 0%, var(--bg-deep) 80%);
  }
  .brand { position: absolute; left: 124px; top: 40px; display: flex; align-items: center; gap: 14px; }
  .brand-mark { width: 40px; height: 40px; background: #bdbdbd; }
  .brand-name {
    font-family: "Cinzel", serif; font-weight: 400; color: #d6d6d6;
    font-size: 25px; line-height: 28px; letter-spacing: 1px;
  }
  .eyebrow {
    position: absolute; left: 141px; top: 222px;
    font-family: "Cinzel", serif; font-size: 15.5px; letter-spacing: 2px;
    color: var(--text-muted);
  }
  .headline {
    position: absolute; left: 134px; top: 262px;
    font-family: "Cinzel", serif; font-weight: 400; font-size: 56px; line-height: 51px;
    letter-spacing: 1.5px; color: var(--text-bright);
  }
  .liaison-form {
    position: absolute; left: 715px; top: 124px; width: 378px; height: 438px;
    border: 1px solid var(--line); background: rgba(0,0,0,0.55);
  }
  .form-title {
    position: absolute; left: 45px; top: 38px;
    font-family: "Cinzel", serif; font-weight: 400; font-size: 23px; color: var(--text-bright);
    letter-spacing: 0.5px;
  }
  .field {
    position: absolute; left: 45px; width: 295px; height: 42px;
    border: 1px solid var(--input-border); background: transparent;
    font-family: "Roboto", sans-serif; font-size: 13px; color: var(--input-text);
    padding: 0 16px; display: flex; align-items: center;
  }
  .field-name { top: 85px; }
  .field-email { top: 143px; }
  .field-phone { top: 197px; }
  .field-description { top: 254px; height: 89px; align-items: flex-start; padding-top: 13px; }
  .submit {
    position: absolute; left: 45px; top: 355px; width: 298px; height: 44px;
    background: linear-gradient(110deg, var(--button-light) 0%, var(--button-light) 40%, var(--button-dark) 75%, #b1b1b4 100%);
    border-radius: 2px; display: flex; align-items: center; justify-content: center;
    font-family: "Cinzel", serif; font-weight: 600; font-size: 15px; color: var(--button-text); letter-spacing: 0.5px;
  }
  .footer {
    position: absolute; left: 0; right: 0; top: 680px; bottom: 0;
    border-top: 1px solid var(--rule);
    display: flex; justify-content: center; padding-top: 20px;
    font-family: "Roboto", sans-serif; font-size: 12.5px; color: var(--footer-text);
  }
</style>
</head>
<body>
<div class="page">
  <div class="backdrop" role="img" aria-label="Dark textured background with soft grey light"></div>

  <header class="brand">
    <span class="brand-mark"></span>
    <span class="brand-name">MARLOW CREST<br>ADVISORY SERVICES</span>
  </header>

  <p class="eyebrow">MARLOW CREST ADVISORY SERVICES</p>
  <h1 class="headline">SEAMLESS<br>MEDICAL EXPERT<br>INTEGRATION</h1>

  <section class="liaison-form">
    <h2 class="form-title">Connect with a Liaison</h2>
    <div class="field field-name">Name*</div>
    <div class="field field-email">Email*</div>
    <div class="field field-phone">Phone number*</div>
    <div class="field field-description">Description of Project</div>
    <div class="submit">SUBMIT</div>
  </section>

  <footer class="footer">© 2026 Marlow Crest Advisory Services. All Rights Reserved</footer>
</div>
</body>
</html>
```